We need a flyer design to promote Penhallow & Tibbs Landscaping and Lawn Maintenance.

The flyer needs to be have:-
1) A great head line ( When quality matters)
2) A really awesome offer ( no obligation free trial mow)
3) A sense of scarcity (Due to time restraints, we can only take limited number of free lawn jobs. This offer is only available to the first 20 callers)
4) A call to action (Call now to avoid disappointment)
5) Contact details (Penhallow & Tibbs Landscaping and Lawn Maintenance 0452 786 305)

The layout of the entire flyer should come across to potential customers as

1) simple to understand what Penhallow & Tibbs offer (not overcrowd with messages; the main aim is to communicate across our services.)

The list of services that Penhallow & Tibbs provide will be:-

- Lawn Mowing - Pruning - Weeding
- Mulching - Edging - Hedging
- Trimming - Fertilising - Garden maintenance
- Weekly, fortnightly or monthly programs

Thank you.

```html
<!DOCTYPE html>
<html lang="en">
<head>
<meta charset="utf-8">
<title>Penhallow &amp; Tibbs — Free Trial Mow Flyer</title>
<link rel="stylesheet" href="https://fonts.googleapis.com/css2?family=Cinzel:wght@400;600;700&family=Oswald:wght@600&display=swap">
<style>
  :root {
    --grass-light: #7fb04a;
    --grass-mid: #4f8a2c;
    --grass-dark: #2f6a1c;
    --paper: #eef2e3;
    --offer-orange: #f2a93b;
    --offer-orange-dark: #d98a1f;
    --cta-blue: #1e8be0;
    --offer-red: #a5170f;
    --ink: #2a1e12;
    --brand-green: #5aa845;
    --white: #ffffff;
  }
  html, body { margin: 0; padding: 0; overflow: hidden; background: var(--paper); }
  .flyer {
    position: relative;
    width: 846px;
    height: 1200px;
    overflow: hidden;
    background: var(--paper);
    font-family: "Cinzel", serif;
  }
  .lawn-backdrop {
    position: absolute; left: 0; top: 0; width: 846px; height: 698px;
    background: linear-gradient(180deg, var(--grass-dark) 0%, var(--grass-mid) 55%, var(--grass-light) 85%, var(--grass-mid) 100%);
  }
  .offer-shapes { position: absolute; left: 0; top: 0; width: 846px; height: 1200px; }
  .line {
    position: absolute; left: 0; width: 100%;
    text-align: center; transform: translateY(-50%);
    margin: 0; white-space: nowrap; line-height: 1;
  }
  .headline { top: 50px; font-size: 40px; color: var(--white); font-weight: 600; font-variant: small-caps; text-transform: lowercase; letter-spacing: 1px; }
  .headline::first-letter { text-transform: uppercase; }
  .offer-kicker { top: 217px; font-size: 34px; color: var(--offer-red); font-weight: 600; }
  .offer-title { top: 279px; font-size: 66px; color: var(--offer-red); font-weight: 700; }
  .scarcity { font-size: 32px; color: var(--ink); font-weight: 700; font-variant: small-caps; }
  .scarcity-1 { top: 366px; }
  .scarcity-2 { top: 408px; }
  .cta-title { top: 514px; font-size: 72px; color: var(--white); font-weight: 600; }
  .cta-sub { top: 572px; font-size: 25px; color: var(--white); font-weight: 600; }
  .phone {
    position: absolute; top: 735px; left: 0; width: 100%;
    display: flex; justify-content: center; align-items: center; gap: 20px;
  }
  .phone-number { font-family: "Oswald", sans-serif; font-weight: 600; font-size: 76px; color: var(--brand-green); letter-spacing: 1px; line-height: 1; }
  .rule { position: absolute; left: 148px; width: 550px; height: 4px; background: var(--brand-green); }
  .rule-top { top: 841px; }
  .rule-bottom { top: 995px; }
  .brand-name { top: 882px; font-size: 44px; color: var(--ink); font-weight: 600; }
  .brand-trade { top: 928px; font-size: 24px; color: var(--ink); font-weight: 600; letter-spacing: 24px; padding-left: 24px; }
  .brand-sub { top: 969px; font-size: 24px; color: var(--ink); font-weight: 600; }
  .services .line { font-size: 20px; color: var(--ink); font-variant: small-caps; letter-spacing: 1px; }
  .services .s1 { top: 1041px; }
  .services .s2 { top: 1072px; }
  .services .s3 { top: 1104px; }
  .services .s4 { top: 1137px; }
  .services .s5 { top: 1169px; }
</style>
</head>
<body>
<main class="flyer">
  <div class="lawn-backdrop" role="img" aria-label="Close-up photograph of a lush green lawn"></div>

  <svg class="offer-shapes" viewBox="0 0 800 1135" preserveAspectRatio="none" aria-hidden="true">
    <polygon class="offer-panel-back" fill="var(--offer-orange-dark)" points="262,92 540,92 600,160 250,160"/>
    <polygon class="offer-panel" fill="var(--offer-orange)" points="25,150 262,142 300,92 500,92 540,150 790,160 720,300 730,430 20,436 90,298"/>
    <polygon class="cta-pointer" fill="var(--offer-orange-dark)" points="365,575 462,575 414,635"/>
    <polygon class="cta-banner" fill="var(--cta-blue)" points="128,438 682,432 648,588 165,580"/>
  </svg>

  <h1 class="line headline">When quality matters</h1>
  <p class="line offer-kicker">NO OBLIGATION</p>
  <h2 class="line offer-title">FREE TRIAL MOW</h2>
  <p class="line scarcity scarcity-1">Offer is limited to the</p>
  <p class="line scarcity scarcity-2">first 20 callers only</p>
  <p class="line cta-title">CALL NOW</p>
  <p class="line cta-sub">TO AVOID DISAPPOINTMENT</p>

  <div class="phone">
    <svg class="phone-icon" width="86" height="86" viewBox="0 0 86 86" aria-hidden="true">
      <circle cx="43" cy="43" r="39" fill="none" stroke="var(--brand-green)" stroke-width="4"/>
      <path fill="var(--brand-green)" d="M34 18 h9 v14 h-6 c-2 6 -2 16 0 22 h6 v14 h-9 c-9 -10 -9 -40 0 -50 z"/>
    </svg>
    <span class="phone-number">0452 786 305</span>
  </div>

  <div class="rule rule-top"></div>
  <p class="line brand-name">Penhallow &amp; Tibbs</p>
  <p class="line brand-trade">LANDSCAPING</p>
  <p class="line brand-sub">and Lawn Maintenance</p>
  <div class="rule rule-bottom"></div>

  <section class="services">
    <p class="line s1">Lawn Mowing - Pruning - Weeding</p>
    <p class="line s2">Mulching - Edging - Hedging</p>
    <p class="line s3">paving solutions</p>
    <p class="line s4">Trimming - Fertilising - Garden maintenance</p>
    <p class="line s5">Weekly, fortnightly or monthly programs</p>
  </section>
</main>
</body>
</html>
```